Website for Apartment Rental in Prague

I would like to create designs of my website focused on luxury apartment rentals in Prague, Czech Republic. I created initial mock-ups, They are all attached. I need to design homepage and subpage. The mock-ups were created by combining elements from different websites that I liked but I need you to create a design that is unique and original. The attached files a only a guidance for the structure of the website but not for the design. Try to be creative.

Industry/Entity Type

Apartment

```html
<!DOCTYPE html>
<html lang="en">
<head>
<meta charset="utf-8">
<title>Lumen Suites – Being Home In Prague</title>
<link href="https://fonts.googleapis.com/css2?family=Roboto+Condensed:wght@400;700&family=Open+Sans:wght@400;600&display=swap" rel="stylesheet">
<style>
  :root {
    --ink: #2b2a2a;
    --bar: #4a4542;
    --footer: #343132;
    --peach: #ebd0c0;
    --peach-deep: #b98a6c;
    --soft: #f4f4f4;
    --line: #dcdcdc;
    --muted: #6d6d6d;
    --white: #ffffff;
  }
  * { margin: 0; padding: 0; box-sizing: border-box; }
  html, body { width: 718px; height: 1200px; overflow: hidden; background: var(--white); }
  body { position: relative; font-family: "Open Sans", Arial, sans-serif; color: var(--ink); }
  .abs { position: absolute; }
  .cond { font-family: "Roboto Condensed", "Arial Narrow", sans-serif; }

  /* top bar */
  .topbar { left: 0; top: 0; width: 718px; height: 24px; background: var(--bar); }
  .topbar__label { left: 96px; top: 6px; font-size: 8px; color: #cfc9c5; }
  .topbar__icons { right: 96px; top: 5px; }

  /* hero */
  .hero { left: 0; top: 24px; width: 718px; height: 333px;
    background: linear-gradient(100deg, #8c8886 0%, #6a6563 35%, #5b5856 55%, #7d7874 80%, #4c4745 100%); }
  .hero::after { content: ""; position: absolute; inset: 0; background: rgba(40,36,34,.35); }
  .logo { left: 0; top: 24px; width: 186px; height: 53px; z-index: 2; }
  .logo__name { left: 0; top: 13px; width: 168px; text-align: center; font-size: 13px; letter-spacing: 2px; color: var(--ink); font-family: "Roboto Condensed", sans-serif; }
  .logo__sub { left: 0; top: 31px; width: 168px; text-align: center; font-size: 5.5px; letter-spacing: 2px; color: var(--ink); font-family: "Roboto Condensed", sans-serif; }
  .nav { left: 199px; top: 46px; display: flex; gap: 18px; z-index: 2; }
  .nav a { font-family: "Roboto Condensed", sans-serif; font-weight: 700; font-size: 7.5px; color: var(--white); text-decoration: none; }
  .hero__rule { left: 96px; width: 526px; height: 1.5px; background: #e9e6e4; z-index: 2; }
  .hero__title { left: 0; top: 150px; width: 718px; text-align: center; z-index: 2; font-weight: 700; font-size: 24px; line-height: 28px; color: var(--white); }
  .tabs { left: 0; top: 235px; width: 718px; height: 30px; z-index: 2; font-size: 8.5px; color: #f1eeec; }
  .tab { position: absolute; top: 7px; }
  .tab--active { left: 142px; top: 0; width: 79px; height: 25px; border: 1px solid #e5e1de; border-radius: 3px; text-align: center; line-height: 23px; }
  .pill { left: 210px; top: 289px; width: 296px; height: 25px; border: 1.5px solid #e9e6e4; border-radius: 13px; z-index: 2; }
  .pill__date { left: 14px; top: 7px; font-size: 7px; color: #eee; }
  .pill__btn { left: 194px; top: -1.5px; width: 102px; height: 25px; border-radius: 13px; background: var(--peach); color: #5a4030; text-align: center; line-height: 25px; font-weight: 700; font-size: 8px; }

  /* vision */
  .vision { left: 0; top: 357px; width: 718px; height: 320px; background: var(--soft); }
  .vision__rule { left: 0; width: 718px; height: 1px; background: var(--line); }
  .vision__title { left: 0; top: 57px; width: 718px; text-align: center; font-weight: 700; font-size: 20px; color: var(--ink); }
  .vision__lead { left: 0; top: 84px; width: 718px; text-align: center; font-size: 9px; color: #333; font-family: "Roboto Condensed", sans-serif; }
  .vision__text { left: 104px; top: 143px; width: 510px; text-align: center; font-size: 6.6px; line-height: 10.5px; color: #555; }
  .photo { background: linear-gradient(160deg, #c9c6c2, #8e8882); }

  /* apartments */
  .apts { left: 0; top: 677px; width: 718px; height: 223px; background: var(--white); }
  .apts__title { left: 207px; top: 10px; font-size: 20px; font-weight: 700; color: var(--ink); }
  .apts__sub { left: 208px; top: 40px; font-size: 9px; color: #333; }
  .card { top: 62px; width: 118px; height: 129px; border: 1px solid #e4e4e4; background: var(--white); box-shadow: 0 1px 2px rgba(0,0,0,.06); }
  .card__img { left: 5px; top: 5px; width: 108px; height: 69px; }
  .card__name { left: 9px; top: 79px; font-size: 9.5px; font-weight: 700; color: var(--ink); }
  .card__text { left: 9px; top: 93px; width: 104px; font-size: 6.5px; line-height: 8px; color: #999; }
  .card__link { left: 9px; top: 113px; font-size: 6.5px; font-weight: 600; color: var(--peach-deep); }

  /* contact form */
  .contact { left: 0; top: 900px; width: 718px; height: 154px; background: var(--peach); }
  .field { background: var(--white); height: 25px; top: 25px; font-size: 7px; color: #b8b8b8; text-align: center; line-height: 25px; }
  .field--area { left: 106px; top: 58px; width: 507px; height: 40px; }
  .submit { left: 330px; top: 106px; width: 58px; height: 24px; border: 1.5px solid var(--white); color: var(--white); font-size: 7px; font-weight: 700; text-align: center; line-height: 21px; }

  /* footer */
  .footer { left: 0; top: 1054px; width: 718px; height: 146px; background: var(--footer); color: #a6a19d; }
  .footer__head { top: 32px; font-size: 8px; font-weight: 600; color: var(--white); }
  .footer__list { top: 49px; list-style: none; font-size: 6.8px; line-height: 10.4px; color: #a6a19d; }
  .footer__list li::before { content: "- "; }
  .footer__list .is-current { color: var(--peach); }
  .newsletter__input { left: 285px; top: 47px; width: 135px; height: 21px; background: #48444 4; background: #474343; }
  .newsletter__btn { left: 285px; top: 72px; width: 54px; height: 22px; background: var(--peach); color: #3a2e28; font-size: 7px; font-weight: 700; text-align: center; line-height: 22px; }
  .footer__info { left: 448px; top: 48px; width: 176px; font-size: 6.6px; line-height: 9px; color: #8e8985; }
  .footer__rule { left: 96px; top: 115px; width: 526px; height: 1px; background: #4a4646; }
  .footer__copy { left: 96px; top: 126px; font-size: 6.5px; color: #77726f; }
  .social { top: 122px; width: 17px; height: 17px; }
</style>
</head>
<body>

  <header>
    <div class="abs topbar">
      <span class="abs topbar__label">Discover Prague</span>
      <svg class="abs topbar__icons" width="34" height="14" viewBox="0 0 34 14" aria-hidden="true">
        <circle cx="5" cy="6" r="4" fill="none" stroke="#cfc9c5" stroke-width="1.2"/>
        <line x1="8" y1="9" x2="11" y2="12" stroke="#cfc9c5" stroke-width="1.3"/>
        <circle cx="27" cy="4.5" r="3" fill="none" stroke="#cfc9c5" stroke-width="1.2"/>
        <path d="M21.5 13 Q27 6 32.5 13" fill="none" stroke="#cfc9c5" stroke-width="1.2"/>
      </svg>
    </div>

    <section class="abs hero" role="img" aria-label="Photo of a couple standing in a bright empty apartment with large windows over the city"></section>

    <div class="abs logo">
      <svg class="abs" width="186" height="53" viewBox="0 0 186 53" aria-hidden="true"><polygon points="0,0 186,0 167,53 0,53" fill="#fff"/></svg>
      <span class="abs logo__name">Lumen</span>
      <span class="abs logo__sub">SUITES</span>
    </div>

    <nav class="abs nav">
      <a href="#">APARTMENTS</a><a href="#">LOCATION</a><a href="#">SERVICES</a><a href="#">GELLERY</a><a href="#">NEWS</a><a href="#">EXCLUSIVE OFFERS &amp; TOURS</a><a href="#">FOR FAMILIES</a><a href="#">CONTACT</a>
    </nav>

    <div class="abs hero__rule" style="top:141px"></div>
    <h1 class="abs hero__title cond">Welcome To Lumen Suites<br>Being Home In Prague</h1>
    <div class="abs hero__rule" style="top:216px"></div>

    <div class="abs tabs">
      <div class="tab tab--active">Check In Date
        <svg class="abs" style="left:36px;top:24px" width="8" height="5" viewBox="0 0 8 5" aria-hidden="true"><polyline points="0,0 4,4 8,0" fill="#5f5a57" stroke="#e5e1de"/></svg>
      </div>
      <span class="tab" style="left:256px">Check Out Date</span>
      <span class="tab" style="left:363px">Adult</span>
      <span class="tab" style="left:428px">Infants</span>
      <span class="tab" style="left:500px">Select Rental Unit</span>
    </div>

    <div class="abs pill">
      <span class="abs pill__date">11 / 17 / 2017</span>
      <span class="abs pill__btn cond">CHACK AVAILABILITY</span>
    </div>
  </header>

  <main>
    <section class="abs vision">
      <div class="abs vision__rule" style="top:37px"></div>
      <svg class="abs" style="left:343px;top:27px" width="32" height="12" viewBox="0 0 32 12" aria-hidden="true"><polyline points="1,11 16,1 31,11" fill="none" stroke="#c9c6c4" stroke-width="3"/><polyline points="14,3 16,1 24,6" fill="none" stroke="#ebcfbf" stroke-width="3"/></svg>
      <h2 class="abs vision__title cond">A Different Vision Of Travelling</h2>
      <p class="abs vision__lead">Lorem ipsum dolor sit amet, consectetur adipiscing elit, sed do eiusmod tempor incididunt ut labore et dolore magna aliqua.</p>
      <div class="abs vision__rule" style="top:117px"></div>
      <svg class="abs" style="left:343px;top:107px" width="32" height="12" viewBox="0 0 32 12" aria-hidden="true"><polyline points="1,11 16,1 31,11" fill="none" stroke="#c9c6c4" stroke-width="3"/><polyline points="14,3 16,1 24,6" fill="none" stroke="#ebcfbf" stroke-width="3"/></svg>
      <p class="abs vision__text">Lorem ipsum dolor sit amet, consectetur adipiscing elit, sed do eiusmod tempor incididunt ut labore et dolore magna aliqua. Ut enim ad minim veniam, quis nostrud exercitation ullamco laboris nisi ut aliquip ex ea commodo consequat.</p>
      <div class="abs photo" style="left:106px;top:184px;width:115px;height:103px;background:linear-gradient(180deg,#5a8fd0 0%,#9bb9dc 35%,#cfc2a8 60%,#8f8574 100%)" role="img" aria-label="Photo of a beige apartment building under blue sky"></div>
      <div class="abs photo" style="left:236px;top:184px;width:115px;height:103px;background:linear-gradient(180deg,#e9eaea 0%,#cfd2d3 55%,#6f7273 100%)" role="img" aria-label="Photo of a grey sofa with a knitted blanket"></div>
      <div class="abs photo" style="left:367px;top:184px;width:115px;height:103px;background:linear-gradient(180deg,#e8e6e3 0%,#d4d0cb 55%,#8a6a4d 100%)" role="img" aria-label="Photo of a bright living room with wooden floor"></div>
      <div class="abs photo" style="left:498px;top:184px;width:115px;height:103px;background:linear-gradient(180deg,#eeeeee 0%,#d8d6d4 55%,#8e8b88 100%)" role="img" aria-label="Photo of a couple with suitcase in a white apartment"></div>
    </section>

    <section class="abs apts">
      <svg class="abs" style="left:0;top:0" width="175" height="223" viewBox="0 0 175 223" role="img" aria-label="Photo of a modern terrace with glass doors and palm plants">
        <defs><linearGradient id="terrace" x1="0" y1="0" x2="0" y2="1"><stop offset="0" stop-color="#4f86c4"/><stop offset=".45" stop-color="#b8c9d6"/><stop offset=".7" stop-color="#6f7a6a"/><stop offset="1" stop-color="#8d8f93"/></linearGradient></defs>
        <polygon points="0,0 175,0 132,223 0,223" fill="url(#terrace)"/>
      </svg>
      <h2 class="abs apts__title cond">Lumen Suites</h2>
      <p class="abs apts__sub cond">Apartment In The Center Of Prague</p>

      <article class="abs card" style="left:208px">
        <div class="abs card__img" style="background:linear-gradient(180deg,#b59a84,#e4dcd2 60%,#5e4a3c)" role="img" aria-label="Photo of a luxury living room"></div>
        <h3 class="abs card__name cond">Brand New Luxury Living</h3>
        <p class="abs card__text">Lorem ipsum dolor sit amet, consectetur adipiscing elit,</p>
        <span class="abs card__link">Details</span>
      </article>
      <article class="abs card" style="left:346px">
        <div class="abs card__img" style="background:linear-gradient(180deg,#4f86c8,#a9c0da 40%,#cdbfa6 70%,#8b8170)" role="img" aria-label="Photo of an apartment building"></div>
        <h3 class="abs card__name cond">Brand New Zen Luxury</h3>
        <p class="abs card__text">Lorem ipsum dolor sit amet, consectetur adipiscing elit,</p>
        <span class="abs card__link">Details</span>
      </article>
      <article class="abs card" style="left:484px">
        <div class="abs card__img" style="background:linear-gradient(180deg,#e7e4e1,#d3cfca 55%,#8a6a4d)" role="img" aria-label="Photo of a bright open living room"></div>
        <h3 class="abs card__name cond">Expedition Top Lock</h3>
        <p class="abs card__text">Lorem ipsum dolor sit amet, consectetur adipiscing elit,</p>
        <span class="abs card__link">Details</span>
      </article>
    </section>

    <section class="abs contact">
      <div class="abs field" style="left:106px;width:161px">Full Name</div>
      <div class="abs field" style="left:278px;width:161px">Email</div>
      <div class="abs field" style="left:451px;width:162px">Phone</div>
      <div class="abs field field--area"></div>
      <div class="abs submit">SUBMIT</div>
    </section>
  </main>

  <footer class="abs footer">
    <h4 class="abs footer__head" style="left:96px">QUICK LINKS</h4>
    <ul class="abs footer__list" style="left:96px">
      <li class="is-current">Apartments</li><li>Loaction</li><li>Services</li><li>Gallery</li><li>News</li>
    </ul>
    <ul class="abs footer__list" style="left:172px">
      <li>Exclusive Offers &amp; Tours</li><li>For Familes</li><li>Contact Us</li>
    </ul>

    <h4 class="abs footer__head" style="left:284px">SIGNUP OUR NEWSLETTER</h4>
    <div class="abs newsletter__input"></div>
    <div class="abs newsletter__btn">SUBMIT</div>

    <h4 class="abs footer__head" style="left:447px">INFORMATIONS ABOUT LUMEN</h4>
    <p class="abs footer__info">Lorem ipsum dolor sit amet, consectetur adipiscing elit, sed do eiusmod tempor incididunt ut labore et dolore magna aliqua. Ut enim ad minim veniam, quis nostrud exercitation ullamco laboris nisi ut aliquip ex ea commodo consequat.</p>

    <div class="abs footer__rule"></div>
    <p class="abs footer__copy">© Copyright 2017 Lumen. All Rights Reserved.</p>
    <span class="abs social" style="left:564px;background:#3b5a98"></span>
    <span class="abs social" style="left:585px;background:#2aa3df"></span>
    <span class="abs social" style="left:605px;background:#1b78b4"></span>
  </footer>

</body>
</html>
```